Advertisements needed for new pub to expand clientele

I need a few different advert. done for my business, can use the same background for all, that covers the following

- New Late Night Menu with Back To School Late Night Prices Thursday-Saturday while bar is open

- $25 gift card to be drawn on September 30th with Liking our facebook page, sharing the ad., and using the hashtag #StirTheSkillet

- Happy Hour Pints $7 & Buy 3 Pints get a free Pretzel Bites between 4:00-5:00 PM

http://www.pinecovetaphouse.com/

https://www.facebook.com/PnCovePub/

Target Market(s)

Restaurant Diners

Industry/Entity Type

Business

Requirements
Must have
• Logo of Pub
• Key information in description for each

```html
<!DOCTYPE html>
<html lang="en">
<head>
<meta charset="utf-8">
<title>Pine Cove Pub – Happy Hour Adverts</title>
<link rel="stylesheet" href="https://fonts.googleapis.com/css2?family=Montserrat:wght@500;600&display=swap">
<style>
  :root {
    --canvas: #ffffff;
    --navy: #282361;
    --charcoal: #231f20;
    --ink: #ffffff;
  }
  * { box-sizing: border-box; margin: 0; padding: 0; }
  html, body {
    width: 1200px;
    height: 1200px;
    overflow: hidden;
    background: var(--canvas);
  }
  body {
    position: relative;
    font-family: "Montserrat", Arial, sans-serif;
    color: var(--ink);
  }
  .advert {
    position: absolute;
    height: 520px;
  }
  .advert--navy { left: 22px; top: 14px; width: 520px; background: var(--navy); }
  .advert--charcoal { left: 564px; top: 15px; width: 520px; background: var(--charcoal); }
  .advert--wide { left: 29px; top: 581px; width: 818px; background: var(--charcoal); }

  .brand-mark {
    position: absolute;
    width: 264px;
    height: 280px;
    display: flex;
    align-items: center;
    justify-content: center;
  }
  .advert--navy .brand-mark,
  .advert--charcoal .brand-mark { left: 126px; top: 18px; }
  .advert--wide .brand-mark { left: 27px; top: 103px; }

  .brand-mark__ring {
    position: absolute;
    left: 7px;
    top: 15px;
    width: 250px;
    height: 250px;
    border: 3px solid var(--ink);
    border-radius: 50%;
  }
  .brand-mark__name {
    position: relative;
    font-weight: 600;
    font-size: 30px;
    line-height: 1.15;
    text-align: center;
    letter-spacing: 0.5px;
  }

  .offer {
    position: absolute;
    font-weight: 600;
    font-size: 24px;
    line-height: 30px;
    text-align: center;
    font-variant-numeric: oldstyle-nums;
  }
  .advert--navy .offer,
  .advert--charcoal .offer { left: 0; right: 0; top: 354px; }
  .advert--wide .offer { left: 400px; width: 342px; top: 204px; }
  .offer sup { font-size: 13px; vertical-align: 9px; }

  .offer-terms {
    position: absolute;
    right: 10px;
    top: 502px;
    font-weight: 500;
    font-size: 10px;
    font-variant-numeric: oldstyle-nums;
  }
  .advert--wide .offer-terms { right: 9px; top: 500px; }
</style>
</head>
<body>
  <section class="advert advert--navy">
    <div class="brand-mark">
      <div class="brand-mark__ring"></div>
      <p class="brand-mark__name">Pine Cove<br>Pub</p>
    </div>
    <p class="offer">Happy Hour Pints $7 &amp; Buy 3 Pints get a<br>free Pretzel Bites<sup>*</sup></p>
    <p class="offer-terms">* offer valid between 4:00-5:00 PM</p>
  </section>

  <section class="advert advert--charcoal">
    <div class="brand-mark">
      <div class="brand-mark__ring"></div>
      <p class="brand-mark__name">Pine Cove<br>Pub</p>
    </div>
    <p class="offer">Happy Hour Pints $7 &amp; Buy 3 Pints get a<br>free Pretzel Bites<sup>*</sup></p>
    <p class="offer-terms">* offer valid between 4:00-5:00 PM</p>
  </section>

  <section class="advert advert--wide">
    <div class="brand-mark">
      <div class="brand-mark__ring"></div>
      <p class="brand-mark__name">Pine Cove<br>Pub</p>
    </div>
    <p class="offer">Happy Hour Pints $7 &amp; Buy 3 Pints<br>get a free Pretzel Bites<sup>*</sup></p>
    <p class="offer-terms">* offer valid between 4:00-5:00 PM</p>
  </section>
</body>
</html>
```